Penrow Insights - what matters when choosing suppliers

We are a consultancy firm called Penrow Insights specializing in customer strategies. We would like to a more illustrative design of the attached graphic.

The graph shows what is important for B2B companies when choosing suppliers. On the left we have the statistical importance and on the right we have the "asked" importance ("on a scale from 1-10, how important is...." ).

Hope it makes sense! :-)

Target Market(s)

B2B Companies

Industry/Entity Type

Business Consultant

```html
<!DOCTYPE html>
<html lang="en">
<head>
<meta charset="utf-8">
<title>Importance of Business Drivers – Penrow Insights</title>
<link rel="stylesheet" href="https://fonts.googleapis.com/css2?family=Arimo:wght@400;700&display=swap">
<style>
  :root {
    --page: #ffffff;
    --ink-grey: #8a96a0;
    --ink-blue: #7fa0e0;
    --calc: #8b969f;
    --asked: #86a8e0;
    --cell-line: #b7c3d6;
    --cell-empty: #ffffff;
    --band-dark: #e4eaf6;
    --band-light: #f5f7fc;
    --rule: #d8dee7;
    --note: #7d8891;
  }
  html, body {
    margin: 0;
    padding: 0;
    width: 1200px;
    height: 846px;
    overflow: hidden;
    background: var(--page);
  }
  .chart {
    position: relative;
    width: 1200px;
    height: 846px;
    font-family: "Arimo", Arial, sans-serif;
    color: var(--ink-grey);
  }
  .chart-title {
    position: absolute;
    top: 54px;
    left: 0;
    width: 1212px;
    margin: 0;
    text-align: center;
    font-size: 43px;
    font-weight: 700;
    letter-spacing: 9.4px;
    color: var(--ink-grey);
  }
  .column-heading {
    position: absolute;
    top: 152px;
    width: 380px;
    margin: 0;
    text-align: center;
    font-size: 20px;
    font-weight: 400;
    letter-spacing: 0.3px;
  }
  .column-heading.calculated { left: 96px; color: var(--ink-grey); }
  .column-heading.asked { left: 712px; color: var(--ink-blue); }
  .heading-rule {
    position: absolute;
    top: 191px;
    display: block;
  }
  .heading-rule.calculated { left: 98px; }
  .heading-rule.asked { left: 715px; }
  .heading-rule line { stroke: var(--rule); stroke-width: 1; }

  .driver-row {
    position: absolute;
    left: 60px;
    width: 1070px;
  }
  .driver-row.dark { background: var(--band-dark); }
  .driver-row.light { background: var(--band-light); }
  .meter {
    position: absolute;
    top: 50%;
    margin-top: -16px;
    display: block;
  }
  .meter.calculated { left: 44px; }
  .meter.asked { left: 655px; }
  .cell-empty { fill: var(--cell-empty); stroke: var(--cell-line); stroke-width: 1; }
  .cell-calc { fill: var(--calc); stroke: var(--calc); stroke-width: 1; }
  .cell-asked { fill: var(--asked); stroke: var(--asked); stroke-width: 1; }
  .fill-calc { fill: var(--calc); }
  .fill-asked { fill: var(--asked); }
  .driver-name {
    position: absolute;
    top: 50%;
    left: 439px;
    width: 200px;
    transform: translateY(-50%);
    text-align: center;
    font-size: 20px;
    line-height: 24px;
    letter-spacing: 0.3px;
    color: var(--ink-grey);
  }
  .method-note {
    position: absolute;
    top: 754px;
    width: 380px;
    margin: 0;
    font-size: 13px;
    line-height: 16.5px;
    color: var(--note);
  }
  .method-note.calculated { left: 96px; text-align: right; }
  .method-note.asked { left: 714px; text-align: left; }
</style>
</head>
<body>
<main class="chart">
  <svg width="0" height="0" style="position:absolute" aria-hidden="true">
    <defs>
      <rect id="cell" width="30" height="30"/>
    </defs>
  </svg>

  <h1 class="chart-title">IMPORTANCE OF BUSINESS DRIVERS</h1>

  <h2 class="column-heading calculated">CALCULATED IMPORTANCE</h2>
  <h2 class="column-heading asked">ASKED IMPORTANCE</h2>

  <svg class="heading-rule calculated" width="372" height="2" aria-hidden="true">
    <line x1="0" y1="1" x2="28" y2="1"/><line x1="37.8" y1="1" x2="65.8" y2="1"/>
    <line x1="75.6" y1="1" x2="103.6" y2="1"/><line x1="113.4" y1="1" x2="141.4" y2="1"/>
    <line x1="151.2" y1="1" x2="179.2" y2="1"/><line x1="189" y1="1" x2="217" y2="1"/>
    <line x1="226.8" y1="1" x2="254.8" y2="1"/><line x1="264.6" y1="1" x2="292.6" y2="1"/>
    <line x1="302.4" y1="1" x2="330.4" y2="1"/><line x1="340.2" y1="1" x2="368.2" y2="1"/>
  </svg>
  <svg class="heading-rule asked" width="372" height="2" aria-hidden="true">
    <line x1="0" y1="1" x2="28" y2="1"/><line x1="37.8" y1="1" x2="65.8" y2="1"/>
    <line x1="75.6" y1="1" x2="103.6" y2="1"/><line x1="113.4" y1="1" x2="141.4" y2="1"/>
    <line x1="151.2" y1="1" x2="179.2" y2="1"/><line x1="189" y1="1" x2="217" y2="1"/>
    <line x1="226.8" y1="1" x2="254.8" y2="1"/><line x1="264.6" y1="1" x2="292.6" y2="1"/>
    <line x1="302.4" y1="1" x2="330.4" y2="1"/><line x1="340.2" y1="1" x2="368.2" y2="1"/>
  </svg>

  <!-- Products -->
  <section class="driver-row dark" style="top:210px;height:100px">
    <svg class="meter calculated" width="372" height="32" viewBox="0 0 372 32" role="img" aria-label="Calculated importance 10 of 10">
      <use href="#cell" class="cell-calc" x="0.5" y="1"/><use href="#cell" class="cell-calc" x="38.3" y="1"/>
      <use href="#cell" class="cell-calc" x="76.1" y="1"/><use href="#cell" class="cell-calc" x="113.9" y="1"/>
      <use href="#cell" class="cell-calc" x="151.7" y="1"/><use href="#cell" class="cell-calc" x="189.5" y="1"/>
      <use href="#cell" class="cell-calc" x="227.3" y="1"/><use href="#cell" class="cell-calc" x="265.1" y="1"/>
      <use href="#cell" class="cell-calc" x="302.9" y="1"/><use href="#cell" class="cell-calc" x="340.7" y="1"/>
    </svg>
    <div class="driver-name">PRODUCTS</div>
    <svg class="meter asked" width="372" height="32" viewBox="0 0 372 32" role="img" aria-label="Asked importance 7.6 of 10">
      <use href="#cell" class="cell-asked" x="0.5" y="1"/><use href="#cell" class="cell-asked" x="38.3" y="1"/>
      <use href="#cell" class="cell-asked" x="76.1" y="1"/><use href="#cell" class="cell-asked" x="113.9" y="1"/>
      <use href="#cell" class="cell-asked" x="151.7" y="1"/><use href="#cell" class="cell-asked" x="189.5" y="1"/>
      <use href="#cell" class="cell-asked" x="227.3" y="1"/>
      <use href="#cell" class="cell-empty" x="265.1" y="1"/><rect class="fill-asked" x="265.1" y="1" width="18" height="30"/>
      <use href="#cell" class="cell-empty" x="302.9" y="1"/><use href="#cell" class="cell-empty" x="340.7" y="1"/>
    </svg>
  </section>

  <!-- Brand -->
  <section class="driver-row light" style="top:314px;height:101px">
    <svg class="meter calculated" width="372" height="32" viewBox="0 0 372 32" role="img" aria-label="Calculated importance 9.4 of 10">
      <use href="#cell" class="cell-empty" x="0.5" y="1"/><rect class="fill-calc" x="18.5" y="1" width="12" height="30"/>
      <use href="#cell" class="cell-calc" x="38.3" y="1"/>
      <use href="#cell" class="cell-calc" x="76.1" y="1"/><use href="#cell" class="cell-calc" x="113.9" y="1"/>
      <use href="#cell" class="cell-calc" x="151.7" y="1"/><use href="#cell" class="cell-calc" x="189.5" y="1"/>
      <use href="#cell" class="cell-calc" x="227.3" y="1"/><use href="#cell" class="cell-calc" x="265.1" y="1"/>
      <use href="#cell" class="cell-calc" x="302.9" y="1"/><use href="#cell" class="cell-calc" x="340.7" y="1"/>
    </svg>
    <div class="driver-name">BRAND</div>
    <svg class="meter asked" width="372" height="32" viewBox="0 0 372 32" role="img" aria-label="Asked importance 0.6 of 10">
      <use href="#cell" class="cell-empty" x="0.5" y="1"/><rect class="fill-asked" x="0.5" y="1" width="19" height="30"/>
      <use href="#cell" class="cell-empty" x="38.3" y="1"/>
      <use href="#cell" class="cell-empty" x="76.1" y="1"/><use href="#cell" class="cell-empty" x="113.9" y="1"/>
      <use href="#cell" class="cell-empty" x="151.7" y="1"/><use href="#cell" class="cell-empty" x="189.5" y="1"/>
      <use href="#cell" class="cell-empty" x="227.3" y="1"/><use href="#cell" class="cell-empty" x="265.1" y="1"/>
      <use href="#cell" class="cell-empty" x="302.9" y="1"/><use href="#cell" class="cell-empty" x="340.7" y="1"/>
    </svg>
  </section>

  <!-- Advice -->
  <section class="driver-row dark" style="top:420px;height:98px">
    <svg class="meter calculated" width="372" height="32" viewBox="0 0 372 32" role="img" aria-label="Calculated importance 3.4 of 10">
      <use href="#cell" class="cell-empty" x="0.5" y="1"/><use href="#cell" class="cell-empty" x="38.3" y="1"/>
      <use href="#cell" class="cell-empty" x="76.1" y="1"/><use href="#cell" class="cell-empty" x="113.9" y="1"/>
      <use href="#cell" class="cell-empty" x="151.7" y="1"/><use href="#cell" class="cell-empty" x="189.5" y="1"/>
      <use href="#cell" class="cell-empty" x="227.3" y="1"/><rect class="fill-calc" x="245.3" y="1" width="12" height="30"/>
      <use href="#cell" class="cell-calc" x="265.1" y="1"/>
      <use href="#cell" class="cell-calc" x="302.9" y="1"/><use href="#cell" class="cell-calc" x="340.7" y="1"/>
    </svg>
    <div class="driver-name">ADVICE</div>
    <svg class="meter asked" width="372" height="32" viewBox="0 0 372 32" role="img" aria-label="Asked importance 4.5 of 10">
      <use href="#cell" class="cell-asked" x="0.5" y="1"/><use href="#cell" class="cell-asked" x="38.3" y="1"/>
      <use href="#cell" class="cell-asked" x="76.1" y="1"/><use href="#cell" class="cell-asked" x="113.9" y="1"/>
      <use href="#cell" class="cell-empty" x="151.7" y="1"/><rect class="fill-asked" x="151.7" y="1" width="16" height="30"/>
      <use href="#cell" class="cell-empty" x="189.5" y="1"/>
      <use href="#cell" class="cell-empty" x="227.3" y="1"/><use href="#cell" class="cell-empty" x="265.1" y="1"/>
      <use href="#cell" class="cell-empty" x="302.9" y="1"/><use href="#cell" class="cell-empty" x="340.7" y="1"/>
    </svg>
  </section>

  <!-- Delivery -->
  <section class="driver-row light" style="top:523px;height:99px">
    <svg class="meter calculated" width="372" height="32" viewBox="0 0 372 32" role="img" aria-label="Calculated importance 2.5 of 10">
      <use href="#cell" class="cell-empty" x="0.5" y="1"/><use href="#cell" class="cell-empty" x="38.3" y="1"/>
      <use href="#cell" class="cell-empty" x="76.1" y="1"/><use href="#cell" class="cell-empty" x="113.9" y="1"/>
      <use href="#cell" class="cell-empty" x="151.7" y="1"/><use href="#cell" class="cell-empty" x="189.5" y="1"/>
      <use href="#cell" class="cell-empty" x="227.3" y="1"/>
      <use href="#cell" class="cell-empty" x="265.1" y="1"/><rect class="fill-calc" x="280.1" y="1" width="15" height="30"/>
      <use href="#cell" class="cell-calc" x="302.9" y="1"/><use href="#cell" class="cell-calc" x="340.7" y="1"/>
    </svg>
    <div class="driver-name">DELIVERY</div>
    <svg class="meter asked" width="372" height="32" viewBox="0 0 372 32" role="img" aria-label="Asked importance 10 of 10">
      <use href="#cell" class="cell-asked" x="0.5" y="1"/><use href="#cell" class="cell-asked" x="38.3" y="1"/>
      <use href="#cell" class="cell-asked" x="76.1" y="1"/><use href="#cell" class="cell-asked" x="113.9" y="1"/>
      <use href="#cell" class="cell-asked" x="151.7" y="1"/><use href="#cell" class="cell-asked" x="189.5" y="1"/>
      <use href="#cell" class="cell-asked" x="227.3" y="1"/><use href="#cell" class="cell-asked" x="265.1" y="1"/>
      <use href="#cell" class="cell-asked" x="302.9" y="1"/><use href="#cell" class="cell-asked" x="340.7" y="1"/>
    </svg>
  </section>

  <!-- Customer service -->
  <section class="driver-row dark" style="top:626px;height:101px">
    <svg class="meter calculated" width="372" height="32" viewBox="0 0 372 32" role="img" aria-label="Calculated importance 0.1 of 10">
      <use href="#cell" class="cell-empty" x="0.5" y="1"/><use href="#cell" class="cell-empty" x="38.3" y="1"/>
      <use href="#cell" class="cell-empty" x="76.1" y="1"/><use href="#cell" class="cell-empty" x="113.9" y="1"/>
      <use href="#cell" class="cell-empty" x="151.7" y="1"/><use href="#cell" class="cell-empty" x="189.5" y="1"/>
      <use href="#cell" class="cell-empty" x="227.3" y="1"/><use href="#cell" class="cell-empty" x="265.1" y="1"/>
      <use href="#cell" class="cell-empty" x="302.9" y="1"/>
      <use href="#cell" class="cell-empty" x="340.7" y="1"/><rect class="fill-calc" x="368.7" y="1" width="2" height="30"/>
    </svg>
    <div class="driver-name">CUSTOMER<br>SERVICE</div>
    <svg class="meter asked" width="372" height="32" viewBox="0 0 372 32" role="img" aria-label="Asked importance 5 of 10">
      <use href="#cell" class="cell-asked" x="0.5" y="1"/><use href="#cell" class="cell-asked" x="38.3" y="1"/>
      <use href="#cell" class="cell-asked" x="76.1" y="1"/><use href="#cell" class="cell-asked" x="113.9" y="1"/>
      <use href="#cell" class="cell-asked" x="151.7" y="1"/>
      <use href="#cell" class="cell-empty" x="189.5" y="1"/>
      <use href="#cell" class="cell-empty" x="227.3" y="1"/><use href="#cell" class="cell-empty" x="265.1" y="1"/>
      <use href="#cell" class="cell-empty" x="302.9" y="1"/><use href="#cell" class="cell-empty" x="340.7" y="1"/>
    </svg>
  </section>

  <p class="method-note calculated">Calculated importance is found through statistical analysis. Partial Lease Squares is used to discover the connection between each business driver and loyalty.</p>
  <p class="method-note asked">Asked Importance is found by simply asking customers how important they find each business driver.</p>
</main>
</body>
</html>
```